Pediatric Pelvic Health Brochure

Looking to design a brochure for Marlow Crest's pelvic health program. I can provide imagery once I see the layout. Our website is marlowcrestpt.example so the look should reflect that

If you see PDF titled blue and word doc you will see what we provided as thoguhts.

Target Market(s)

parents of children

Industry/Entity Type

Health And Wellness

Font styles to use
Serif

Requirements
Must have
• clear call outs - easy to read with copy,
Should not have
• not look bland or dated

```html
<!DOCTYPE html>
<html lang="en">
<head>
<meta charset="utf-8">
<title>Pediatric Pelvic Health – Marlow Crest Brochure</title>
<link rel="stylesheet" href="https://fonts.googleapis.com/css2?family=Playfair+Display:wght@700;800;900&family=Tinos:wght@400;700&display=swap">
<style>
  :root {
    --bg: #dfe9ec;
    --blue: #23b4e3;
    --blue-deep: #1ea1d4;
    --blue-light: #43cdf2;
    --blue-pale: #66d6f5;
    --blob: #0bc6f0;
    --navy: #233f93;
    --ink: #1b1b1f;
    --icon: #16a9df;
    --paper: #eceded;
    --paper-white: #fbfbfb;
  }
  * { box-sizing: border-box; margin: 0; padding: 0; }
  html, body { width: 1200px; height: 900px; overflow: hidden; }
  body { background: var(--bg); font-family: "Tinos", "Times New Roman", serif; color: var(--navy); position: relative; }

  .brochure { position: absolute; left: 60px; top: 100px; width: 1080px; height: 700px; display: flex; box-shadow: 0 14px 40px rgba(20,60,80,.18); }
  .panel { position: relative; width: 360px; height: 700px; overflow: hidden; }

  /* Panel 1 – diagnoses */
  .panel--diagnoses { background: var(--blue-deep); }
  .panel--diagnoses .edge-band { position: absolute; left: 0; top: 0; width: 30px; height: 100%; background: #1b95c8; }
  .panel--diagnoses .sheet { position: absolute; left: 44px; top: 40px; width: 300px; height: 600px; background: var(--paper); }
  .diagnoses-tag { position: absolute; right: -16px; top: -14px; width: 170px; height: 130px; }
  .diagnoses-tag span { position: absolute; left: 30px; top: 36px; width: 120px; font-family: "Playfair Display", serif; font-style: normal; font-weight: 800; font-size: 13px; line-height: 1.15; text-transform: uppercase; color: var(--navy); }
  .diagnosis-list { position: absolute; left: 16px; top: 124px; right: 16px; list-style: none; }
  .diagnosis-list li { display: flex; align-items: flex-start; gap: 9px; font-size: 13px; line-height: 1.2; margin-bottom: 9px; }
  .diagnosis-list svg { flex: 0 0 16px; width: 16px; height: 16px; margin-top: 1px; }

  /* Panel 2 – contact */
  .panel--contact { background: var(--blue); }
  .panel--contact .sheet { position: absolute; left: 24px; top: 40px; width: 312px; height: 600px; background: linear-gradient(180deg, var(--paper-white), #e4e4e5); overflow: hidden; }
  .contact-wave { position: absolute; left: 0; top: 0; width: 312px; height: 170px; }
  .contact-title { position: absolute; left: 0; right: 0; top: 176px; text-align: center; font-family: "Tinos", serif; font-weight: 700; font-size: 25px; letter-spacing: 1px; color: var(--ink); }
  .contact-offer { position: absolute; left: 32px; right: 28px; top: 220px; font-weight: 700; font-size: 17px; line-height: 1.2; color: var(--navy); }
  .contact-row { position: absolute; left: 28px; right: 20px; display: flex; align-items: center; gap: 22px; font-weight: 700; font-size: 16px; line-height: 1.2; color: var(--navy); }
  .contact-row svg { flex: 0 0 42px; width: 42px; height: 42px; }
  .contact-row--phone { top: 326px; }
  .contact-row--address { top: 404px; }
  .contact-row--web { top: 500px; }

  /* Panel 3 – cover */
  .panel--cover { background: var(--blue-light); }
  .cover-tint { position: absolute; left: 0; top: 0; width: 110px; height: 520px; background: var(--blue-pale); }
  .brand { position: absolute; left: 26px; top: 30px; display: flex; align-items: center; gap: 10px; }
  .brand-square { width: 28px; height: 28px; background: var(--ink); }
  .brand-name { font-family: "Tinos", serif; font-size: 22px; color: var(--ink); line-height: 1; }
  .brand-sub { position: absolute; left: 64px; top: 58px; font-size: 7px; letter-spacing: .6px; text-transform: uppercase; color: var(--ink); }
  .cover-card { position: absolute; left: 40px; top: 116px; width: 280px; height: 520px; background: var(--paper-white); }
  .cover-title { position: absolute; left: 24px; top: 22px; font-family: "Playfair Display", serif; font-weight: 900; font-size: 46px; line-height: 1.02; color: var(--navy); }
  .cover-subtitle { position: absolute; left: 26px; top: 180px; font-size: 10px; letter-spacing: .6px; color: var(--navy); }
  .cover-photo { position: absolute; left: 30px; top: 212px; width: 220px; height: 220px; border-radius: 50%; background: radial-gradient(circle at 60% 40%, #e9eef8 0%, #c5d3ec 55%, #9fb6dd 100%); }
  .cover-url { position: absolute; left: 0; right: 0; bottom: 34px; text-align: center; font-size: 14px; color: var(--navy); }
</style>
</head>
<body>
<main class="brochure">

  <section class="panel panel--diagnoses" aria-label="Diagnoses we treat">
    <div class="edge-band"></div>
    <div class="sheet">
      <div class="diagnoses-tag">
        <svg viewBox="0 0 170 130" width="170" height="130" aria-hidden="true">
          <path d="M18 20 C60 0 130 4 168 18 L170 118 C140 108 120 128 90 120 C60 112 40 126 22 104 C6 84 10 50 18 20 Z" fill="var(--blob)"/>
        </svg>
        <span>We treat a range of diagnoses</span>
      </div>
      <ul class="diagnosis-list">
        <li><svg viewBox="0 0 16 16"><circle cx="5" cy="6" r="3" fill="var(--icon)"/><circle cx="11" cy="10" r="3" fill="var(--icon)"/></svg>Constipation</li>
        <li><svg viewBox="0 0 16 16"><path d="M8 1 C11 6 13 8 13 11 A5 5 0 0 1 3 11 C3 8 5 6 8 1Z" fill="var(--icon)"/></svg>Increased urinary frequency</li>
        <li><svg viewBox="0 0 16 16"><circle cx="8" cy="8" r="6" fill="none" stroke="var(--icon)" stroke-width="2"/><path d="M5 9 A3 3 0 0 0 11 9" fill="none" stroke="var(--icon)" stroke-width="1.6"/></svg>Night-time incontinence, bed-wetting, or enuresis</li>
        <li><svg viewBox="0 0 16 16"><path d="M8 1 L10 6 L15 6 L11 9.5 L12.5 15 L8 11.5 L3.5 15 L5 9.5 L1 6 L6 6Z" fill="var(--icon)"/></svg>Day-time incontinence</li>
        <li><svg viewBox="0 0 16 16"><ellipse cx="8" cy="9" rx="6" ry="5" fill="var(--icon)"/></svg>Giggle incontinence</li>
        <li><svg viewBox="0 0 16 16"><rect x="3" y="3" width="5" height="11" fill="var(--icon)"/><rect x="8" y="9" width="6" height="5" fill="var(--icon)"/></svg>Incontinence in the athletic female child or teenager</li>
        <li><svg viewBox="0 0 16 16"><rect x="1" y="7" width="6" height="8" fill="var(--icon)"/><rect x="9" y="3" width="6" height="12" fill="var(--icon)"/></svg>Waking up in the night to urinate or nocturia</li>
        <li><svg viewBox="0 0 16 16"><rect x="3" y="2" width="10" height="12" fill="none" stroke="var(--icon)" stroke-width="1.8"/><path d="M5 6h6M5 9h6" stroke="var(--icon)" stroke-width="1.4"/></svg>Difficulty with urination: straining, slow flow, pain during or after urination</li>
        <li><svg viewBox="0 0 16 16"><circle cx="8" cy="5" r="3" fill="var(--icon)"/><path d="M2 15 C3 9 13 9 14 15Z" fill="var(--icon)"/></svg>Reduced sensation of bladder or bowel fullness</li>
        <li><svg viewBox="0 0 16 16"><circle cx="8" cy="8" r="6" fill="none" stroke="var(--icon)" stroke-width="1.8"/><path d="M5 11 A3 3 0 0 1 11 11" fill="none" stroke="var(--icon)" stroke-width="1.6"/></svg>Pain in the abdomen, bladder or lower back</li>
        <li><svg viewBox="0 0 16 16"><path d="M8 2 L15 14 L1 14Z" fill="none" stroke="var(--icon)" stroke-width="1.8"/></svg>Fecal incontinence</li>
        <li><svg viewBox="0 0 16 16"><circle cx="8" cy="8" r="5" fill="none" stroke="var(--icon)" stroke-width="1.8"/><path d="M8 1v3M8 12v3M1 8h3M12 8h3" stroke="var(--icon)" stroke-width="1.6"/></svg>Treatment after pediatric pelvic surgeries</li>
      </ul>
    </div>
  </section>

  <section class="panel panel--contact" aria-label="Contact us">
    <div class="sheet">
      <svg class="contact-wave" viewBox="0 0 312 170" aria-hidden="true">
        <path d="M0 0 H312 V150 C270 176 220 130 160 140 C100 150 40 170 0 150 Z" fill="var(--blob)"/>
      </svg>
      <h2 class="contact-title">CONTACT US</h2>
      <p class="contact-offer">We offer a FREE 15 minute consultation to help you determine if therapy is right for you.</p>
      <div class="contact-row contact-row--phone">
        <svg viewBox="0 0 42 42" aria-hidden="true"><rect x="6" y="11" width="30" height="21" fill="none" stroke="var(--icon)" stroke-width="2.5"/><path d="M6 11 L21 24 L36 11" fill="none" stroke="var(--icon)" stroke-width="2.5"/></svg>
        <span>555.014.2870</span>
      </div>
      <div class="contact-row contact-row--address">
        <svg viewBox="0 0 42 42" aria-hidden="true"><path d="M21 39 C21 39 8 24 8 16 A13 13 0 0 1 34 16 C34 24 21 39 21 39Z" fill="none" stroke="var(--icon)" stroke-width="2.5"/><circle cx="21" cy="16" r="5" fill="none" stroke="var(--icon)" stroke-width="2.5"/></svg>
        <span>48 Harbor Lane<br>Ground Floor<br>Brookfield, NY 10099</span>
      </div>
      <div class="contact-row contact-row--web">
        <svg viewBox="0 0 42 42" aria-hidden="true"><circle cx="21" cy="21" r="16" fill="none" stroke="var(--icon)" stroke-width="2.5"/><ellipse cx="21" cy="21" rx="7" ry="16" fill="none" stroke="var(--icon)" stroke-width="2"/><path d="M5 21h32M8 13h26M8 29h26" stroke="var(--icon)" stroke-width="2"/></svg>
        <span>marlowcrestpt.example</span>
      </div>
    </div>
  </section>

  <section class="panel panel--cover" aria-label="Brochure cover">
    <div class="cover-tint"></div>
    <div class="brand">
      <span class="brand-square"></span>
      <span class="brand-name">Marlow Crest</span>
    </div>
    <p class="brand-sub">Physical and Aquatic Therapy</p>
    <div class="cover-card">
      <h1 class="cover-title">Pediatric<br>Pelvic<br>Health</h1>
      <p class="cover-subtitle">Treating Infants, Children &amp; Adolescents</p>
      <div class="cover-photo" role="img" aria-label="Photo of two smiling clinicians in white coats"></div>
      <p class="cover-url">marlowcrestpt.example</p>
    </div>
  </section>

</main>
</body>
</html>
```